Design Creative Banner or Gif Ads. 3 Designs To Be Selected

Come up with some creative banner ads for stonewell.co.nz

*At least 3 different winning banners will be chosen*

Please provide banner ads / gif ads in common google ads / website banner formats.

They can be gif or static but must stand out while still maintaining clear clean text and visuals, with a premium professional feel (please avoid clip art or anything that gives a cheap message).

Please keep in mind that these will likely be small ads so text needs to be large and if there's there a lot of text then use multiple frames/ pages as submit as a gif.

Style
Minimal & clean lines
Architectural or realistic images
Avoid cartoon styles, clipart, or anything that looks cheap

Font
Nexa or Montserrat or similar

Tone
Premium, serious, trustworthy — fits new builds

Colours
Option 1: Deep Navy (trust & quality) & lighter blues and warm grey
Option 2: Open to bright colours to help the ads stand out, such as (but not limited to) bright pink with black, yellow, fluorescent green, provided the messaging is still done professionally.
Our logo is attached (Stone Well Logo)

Display Sizes
Ad specs for file sizes should be file formats like JPEG, GIF, and PNG, with animations limited to a max of 30 seconds or less.
We will need several different ad sizes provided for each of the 3 selected winning designs.

• Medium Rectangle: 300 × 250 pixels
• Leaderboard: 728 × 90 pixels
• Desktop Banner ad image: (640x360 pixels)
• Desktop Banner ad image 2: (300x600 pixels)
• Possibly one or two other sizes

Flexibility to be creative
The ad text, words, upper/lower case, layout, colour, theme, and images can be adjusted to how you think it will look best. The follow example ads are just examples of what we are after but we are keen to see what you can create.

Recommendations at this point:
1. Avoid text heavy
2. Looking for more Gif ads
3. Imaging: if possible use real stock photo's rather than AI

Themes:

1
Building Soon? Start Here
Free Build Planning Pack:
✓ Build Cost Calculator
✓ Hidden Cost Checklist
✓ Builder Comparison Guide
Build With Confidence
Download Free

2
Before You Choose A Builder
Compare Price, Scope, Risk & Value
Avoid Costly Mistakes
Choose The Right Builder With Confidence
Download The Free Guide

3
Planning A New Build?
Avoid These Common Mistakes:
✗ Hidden Exclusions
✗ Missing Scope
✗ Unrealistic Allowances
✗ Budget Blowouts
Download The Free Guide

4
Before You Buy Land
Know what it could cost to build.
Avoid Costly Building Mistakes
Download Our Free Guides

5
Know Your Build Budget?
• Free Build Cost Calculator
• Hidden Cost Checklist
• Build Planning Tools
Calculate Costs (Download)

Target Market(s)

Landowners looking to build

Industry/Entity Type

Building

Font styles to use
Other font styles liked:
• Nexa or Montserrat or similar

Requirements
Should not have
• Avoid cartoon styles, clipart, or anything that looks cheap

```html
<!DOCTYPE html>
<html lang="en">
<head>
<meta charset="utf-8">
<title>Stone Well – Building Soon? Start Here</title>
<link rel="stylesheet" href="https://fonts.googleapis.com/css2?family=Montserrat:wght@600;700;800;900&family=Open+Sans:wght@400;500&family=Oswald:wght@600&display=swap">
<style>
  :root {
    --navy-deep: #0c2a4a;
    --navy: #12385f;
    --blue-mid: #1f5fa8;
    --blue-bright: #2a7fd6;
    --blue-light: #8fb6e0;
    --ink-dark: #163a55;
    --paper: #e9eef2;
    --white: #ffffff;
    --cta-green: #22d814;
    --cta-text: #0b2a1a;
    --page: #ffffff;
  }
  * { margin: 0; padding: 0; box-sizing: border-box; }
  html, body {
    width: 1200px; height: 1200px; overflow: hidden;
    background: var(--page);
  }
  .canvas { position: relative; width: 1200px; height: 1200px; }
  .banner {
    position: absolute; left: 0; top: 281px;
    width: 1200px; height: 637px; overflow: hidden;
    font-family: "Montserrat", sans-serif; color: var(--white);
  }
  .blueprint-backdrop {
    position: absolute; inset: 0;
    background:
      radial-gradient(ellipse at 75% 55%, var(--blue-bright) 0%, var(--blue-mid) 35%, transparent 70%),
      linear-gradient(90deg, var(--navy-deep) 0%, var(--navy) 40%, var(--blue-mid) 100%);
  }
  .brand-tab {
    position: absolute; left: 0; top: 0;
    width: 386px; height: 77px;
    background: linear-gradient(90deg, #f4f6f8, #e6ebf0);
    border-radius: 0 40px 40px 0;
  }
  .brand-mark {
    position: absolute; left: 44px; top: 16px;
    width: 44px; height: 44px; background: var(--navy);
  }
  .brand-name {
    position: absolute; left: 104px; top: 14px;
    font-size: 30px; font-weight: 700; color: var(--navy-deep);
    letter-spacing: 0.2px; line-height: 1;
  }
  .brand-tagline {
    position: absolute; left: 105px; top: 53px;
    font-size: 8.5px; font-weight: 700; color: var(--blue-mid);
    letter-spacing: 0.3px; text-transform: uppercase;
  }
  .headline {
    position: absolute; left: 46px; top: 112px;
    font-weight: 800; line-height: 0.88; font-size: 86px;
    text-transform: uppercase;
  }
  .headline .line { display: block; }
  .headline .line--accent {
    color: var(--blue-light); font-size: 76px; margin-top: -2px;
  }
  .divider {
    position: absolute; left: 48px; top: 343px;
    width: 514px; height: 2px; background: rgba(143,182,224,0.7);
  }
  .pack-title {
    position: absolute; left: 48px; top: 364px;
    font-size: 18px; font-weight: 700; color: var(--blue-light);
    text-transform: uppercase; letter-spacing: 0.3px;
  }
  .pack-list {
    position: absolute; left: 48px; top: 396px;
    list-style: none; font-family: "Open Sans", sans-serif;
    font-size: 20px; font-weight: 500;
  }
  .pack-list li {
    display: flex; align-items: center; gap: 12px;
    height: 31px;
  }
  .pack-list svg { width: 20px; height: 20px; flex: none; }
  .confidence {
    position: absolute; left: 52px; top: 500px;
    font-size: 33px; font-weight: 800; text-transform: uppercase;
  }
  .cta {
    position: absolute; left: 52px; top: 558px;
    width: 250px; height: 48px; border-radius: 9px;
    background: var(--cta-green);
    display: flex; align-items: center; justify-content: center;
    font-size: 20px; font-weight: 800; color: var(--cta-text);
    text-transform: uppercase; box-shadow: 0 2px 6px rgba(0,0,0,0.3);
  }
  .cost-reveal { position: absolute; left: 0; top: 0; width: 1200px; height: 637px; }
  .cost-reveal text {
    font-family: "Oswald", sans-serif; font-weight: 600;
    fill: var(--ink-dark); font-size: 36px; text-anchor: middle;
  }
</style>
</head>
<body>
<div class="canvas">
  <section class="banner">
    <div class="blueprint-backdrop" role="img" aria-label="Blueprint house plan drawing in glowing blue tones"></div>

    <svg class="cost-reveal" viewBox="0 0 1200 637" aria-hidden="true">
      <polygon points="594,325 894,155 1158,349 888,557" fill="var(--navy-deep)"/>
      <polygon points="672,391 900,253 1110,391 888,557" fill="var(--paper)"/>
      <g transform="translate(895,400) rotate(-27)">
        <text y="-34">DON'T MISS</text>
        <text y="10">WHAT IT REALLY</text>
        <text y="54">COSTS.</text>
      </g>
    </svg>

    <div class="brand-tab">
      <div class="brand-mark"></div>
      <div class="brand-name">Stone Well</div>
      <div class="brand-tagline">Compare quotes from trusted builders</div>
    </div>

    <h1 class="headline">
      <span class="line">Building</span>
      <span class="line">Soon?</span>
      <span class="line line--accent">Start Here.</span>
    </h1>
    <div class="divider"></div>

    <p class="pack-title">Free Build Planning Pack:</p>
    <ul class="pack-list">
      <li><svg viewBox="0 0 20 20"><path d="M2 11 L7 16 L18 3" fill="none" stroke="#fff" stroke-width="2.4" stroke-linecap="round" stroke-linejoin="round"/></svg>Build Cost Calculator</li>
      <li><svg viewBox="0 0 20 20"><path d="M2 11 L7 16 L18 3" fill="none" stroke="#fff" stroke-width="2.4" stroke-linecap="round" stroke-linejoin="round"/></svg>Hidden Cost Checklist</li>
      <li><svg viewBox="0 0 20 20"><path d="M2 11 L7 16 L18 3" fill="none" stroke="#fff" stroke-width="2.4" stroke-linecap="round" stroke-linejoin="round"/></svg>Builder Comparison Guide</li>
    </ul>

    <p class="confidence">Build With Confidence</p>
    <div class="cta">Download Free</div>
  </section>
</div>
</body>
</html>
```